Creative UI design for web application

I need a new UI design for my web application. It will be used by small and micro business owners to plan & implement growth tactics.

I've attached the current design (which I'm open to be changed) - but in particular I need to design the centre of the screen, where the work actually happens.

There needs to be place for a title (YOUR BUSINESS) and description (say 1-2 paragraphs of text) - and am happy to include icons or imagery where makes sense. It may make sense for the user to be able to upload their business logo and name, for example.

This screen will be used by the business owner to understand the real value they offer potential customers and their point of difference - why they exist and why potential customers should care.

They'll use the information they put into this screen to plan things like their messaging.

Following that, there needs to be 2 sections in the dashboard.

The first section is titled "WHO YOU ARE"

The first section will include a number of boxes that the user can input information into, as follows:

- Logo
- Business name
- Business tag line
- Business vision
- Business bio
- Brand colours (these should end up as swatches based on the colour code they enter) - the colour code for each colour swatch should also be visible.
- Key competitors
- SWOT analysis (boxes to enter their strengths, weaknesses, opportunities and threats).

The second section is titled "WHY YOU EXIST"

The second section will include a number of boxes that the user can input information (text) into, as follows:

- Who are your ideal customers?
- What problem are you trying to solve for them?
- What pain points will this remove for them?
- How do you solve it?
- How else could this problem be solved?
- Who offers these other solutions?
- Why is your solution better?
- How much does your solution cost?
- What value are you providing to justify this cost?
- How will this make their life/job easier/better?

They should be able to write a decent amount of information in the boxes.

There should ideally be a place for a description for each of these text fields (for both section 1 & 2) as well so I can give them a little bit more direction around what to put in the box. Alternatively there could be a little icon (say a question mark or "i") that they could click on to view instructions. The instructions will be around 2-4 sentences long for each text field.

You have 2 options:

a) This all needs to appear on the one screen, and the navigation needs to be visible (as per the example attached but feel free to recreate this navigation)

Note: the page can scroll below the fold - but please provide the design for the full length of the page.

b) Potentially the 2 sections could actually be in 2 different items in the menu - YOUR BUSINESS and YOUR VALUE (which would sit next to YOUR BUSINESS and before YOUR CUSTOMER in the screenshot provided). feel free to design them as 2 separate screens if you prefer.

I have attached a screenshot of the app as it stands today (screen shot 2017) which would still exist in the new design but under a different section (the learn section from the plan2 mockup attached)

I have mocked up how this new screen could look if broken into 2 and that's also attached. If you can make this come to life - and look more engaging that would be helpful! :)

Target Market(s)

Small and micro business owners

Industry/Entity Type

Marketing

Number of Pages Required

1 page

Font styles to use
Sans Serif
Other font styles liked:
• Montserrat

Colors
87cfc6
d2a4cc
ffffff
85cae6
e8e8e8
5c5c5c

Requirements
Must have
• Use of my brand colours: #cc8eb2, #76d6c8, #68c7ff as well as white and #595959. Must be visually pleasing / engaging, designed for desktop (as it's a desktop application), really easy to use / navigate.
• Use font Montserrat light & Montserrat Regular or Bold. Mostly should be Montserrat light.
Nice to have
• Would be nice to see how this would look on mobile (as the application is responsive) but this is not mandatory.
Should not have
• Should not look too corporate or dry.

```html
<!DOCTYPE html>
<html lang="en">
<head>
<meta charset="utf-8">
<title>Tendril – Your Business</title>
<link href="https://fonts.googleapis.com/css2?family=Montserrat:wght@300;400;600&display=swap" rel="stylesheet">
<style>
:root{
  --teal:#76d6c8;
  --pink:#cc8eb2;
  --blue:#68c7ff;
  --ink:#595959;
  --ink-soft:#8a8a8a;
  --line:#e8e8e8;
  --dark:#3b3b3b;
  --white:#ffffff;
  --page:#f7f7f7;
}
*{box-sizing:border-box;margin:0;padding:0}
html,body{width:1200px;height:2660px;overflow:hidden}
body{font-family:"Montserrat",sans-serif;font-weight:300;color:var(--ink);background:var(--page);position:relative}

.topbar{height:56px;background:var(--dark);display:flex;align-items:center;justify-content:space-between;padding:0 40px}
.brand{color:var(--white);font-weight:600;font-size:18px;letter-spacing:2px;display:flex;align-items:center;gap:10px}
.brand-dot{width:12px;height:12px;background:var(--teal)}
.topnav{display:flex;gap:30px}
.topnav a{color:var(--white);text-decoration:none;font-size:11px;font-weight:400;letter-spacing:1px;display:flex;align-items:center;gap:6px}
.topnav svg{width:12px;height:12px}

.subnav{height:40px;background:var(--teal);display:flex;padding:0 60px}
.subnav a{width:216px;text-align:center;line-height:40px;color:var(--white);font-size:11px;font-weight:400;letter-spacing:1px;text-decoration:none}
.subnav a.active{background:var(--pink)}

.main{width:1080px;margin:0 auto}

.intro{margin-top:16px;height:288px;background:var(--white);border:1px solid var(--line);display:flex;align-items:center;padding:0 30px;gap:30px}
.intro-logo{width:150px;height:150px;border-radius:50%;border:1px solid #d6d6d6;display:flex;align-items:center;justify-content:center;font-size:18px;font-weight:400;color:var(--ink);flex:none}
.intro-text{flex:1}
.intro-title{color:var(--pink);font-size:13px;font-weight:400;letter-spacing:1px;margin-bottom:14px}
.intro-text p{font-size:12px;line-height:20px;margin-bottom:14px}
.intro-photo{width:320px;height:200px;flex:none;background:linear-gradient(135deg,#cfece8,#7cc7c2 55%,#4e9c9f)}

.section-title{font-size:15px;font-weight:400;letter-spacing:1.5px;margin:30px 0 16px}
.section-title.who{color:var(--teal)}
.section-title.why{color:var(--pink)}

.grid{display:grid;grid-template-columns:1fr 1fr;column-gap:40px;row-gap:20px}
.field{background:var(--white);border:2px solid var(--teal);padding:22px 22px;position:relative}
.field.h170{height:170px}
.field.full{margin-top:20px}
.field-label{font-size:13px;font-weight:400;color:var(--ink);margin-bottom:14px}
.field-hint{font-size:11px;line-height:18px;color:var(--ink-soft);max-width:440px}

.brand-colours{min-height:96px;display:flex;justify-content:space-between;align-items:flex-start;gap:30px;padding:20px 22px}
.brand-colours .field-label{margin-bottom:10px}
.brand-colours .field-hint{max-width:none}
.swatches{display:flex;border:1px solid var(--line);margin-top:4px;flex:none}
.swatches span{width:14px;height:14px}

.swot{margin-top:20px;height:404px;background:var(--teal);padding:0 30px 30px}
.swot-head{height:54px;line-height:54px;color:var(--white);font-size:13px;font-weight:400}
.swot .grid{column-gap:30px}
.swot .field{height:150px;border-color:var(--white)}

.why .field{border-color:var(--pink);height:160px}
.why .field-label{padding-right:30px}
.help{position:absolute;top:18px;right:18px;width:16px;height:16px}

.save{display:block;width:200px;height:50px;margin:30px auto 0;background:var(--pink);color:var(--white);border:none;font-family:"Montserrat",sans-serif;font-weight:400;font-size:13px;letter-spacing:.5px}

.footer{position:absolute;left:0;bottom:0;width:1200px;height:60px;background:var(--dark);color:var(--white);font-size:11px;text-align:center;line-height:60px}
</style>
</head>
<body>

<header class="topbar">
  <div class="brand"><span class="brand-dot"></span>TENDRIL</div>
  <nav class="topnav">
    <a href="#"><svg viewBox="0 0 12 12"><rect x="1" y="2" width="10" height="9" fill="none" stroke="#fff"/><line x1="1" y1="5" x2="11" y2="5" stroke="#fff"/></svg>PLAN</a>
    <a href="#"><svg viewBox="0 0 12 12"><path d="M1 3h4l1 1 1-1h4v7H1z" fill="none" stroke="#fff"/></svg>LEARN</a>
    <a href="#"><svg viewBox="0 0 12 12"><rect x="1.5" y="1.5" width="9" height="9" fill="none" stroke="#fff"/><line x1="6" y1="3.5" x2="6" y2="8.5" stroke="#fff"/><line x1="3.5" y1="6" x2="8.5" y2="6" stroke="#fff"/></svg>GENERATE</a>
    <a href="#"><svg viewBox="0 0 12 12"><circle cx="6" cy="4" r="2.5" fill="#fff"/><path d="M1.5 11c0-3 2-4.5 4.5-4.5s4.5 1.5 4.5 4.5z" fill="#fff"/></svg>MY PROFILE</a>
    <a href="#"><svg viewBox="0 0 12 12"><path d="M5 2H2v8h3M5 6h6M8.5 3.5 11 6 8.5 8.5" fill="none" stroke="#fff"/></svg>LOGOUT</a>
  </nav>
</header>

<nav class="subnav">
  <a href="#" class="active">YOUR BUSINESS</a>
  <a href="#">YOUR PRODUCTS</a>
  <a href="#">YOUR CUSTOMERS</a>
  <a href="#">YOUR GOALS</a>
  <a href="#">YOUR PLAN</a>
</nav>

<main class="main">
  <section class="intro">
    <div class="intro-logo">Lumen Co</div>
    <div class="intro-text">
      <h1 class="intro-title">BUILD YOUR BUSINESS STORY</h1>
      <p>Tell us who you are and what makes your business different. The answers you give here shape your messaging, guide your growth tactics and help you explain clearly why customers should care about what you offer.</p>
      <p>Work through each box at your own pace. Click the small help icon for tips, save as you go and return whenever your business changes.</p>
    </div>
    <div class="intro-photo" role="img" aria-label="Business workspace photo in soft teal tones"></div>
  </section>

  <h2 class="section-title who">WHO YOU ARE</h2>
  <div class="grid">
    <div class="field h170"><div class="field-label">Business Name :</div><p class="field-hint">Describe this in a few clear sentences so your message stays simple, honest and easy for customers to follow.</p></div>
    <div class="field h170"><div class="field-label">Business tag line :</div><p class="field-hint">Describe this in a few clear sentences so your message stays simple, honest and easy for customers to follow.</p></div>
    <div class="field h170"><div class="field-label">Business Vision :</div><p class="field-hint">Describe this in a few clear sentences so your message stays simple, honest and easy for customers to follow.</p></div>
    <div class="field h170"><div class="field-label">Business Bio :</div><p class="field-hint">Describe this in a few clear sentences so your message stays simple, honest and easy for customers to follow.</p></div>
  </div>

  <div class="field full brand-colours">
    <div>
      <div class="field-label">Brand colours :</div>
      <p class="field-hint">Describe this in a few clear sentences so your message stays simple, honest and easy for customers to follow.</p>
    </div>
    <div class="swatches">
      <span style="background:#595959"></span><span style="background:#76d6c8"></span><span style="background:#68c7ff"></span><span style="background:#cc8eb2"></span><span style="background:#f2b84b"></span><span style="background:#e46a4f"></span><span style="background:#e8e8e8"></span><span style="background:#ffffff"></span>
    </div>
  </div>

  <div class="field full" style="height:160px">
    <div class="field-label">Key Competitors :</div>
    <p class="field-hint">Describe this in a few clear sentences so your message stays simple, honest and easy for customers to follow.</p>
  </div>

  <section class="swot">
    <div class="swot-head">SWOT Analysis</div>
    <div class="grid">
      <div class="field"><div class="field-label">Strengths :</div><p class="field-hint">Describe this in a few clear sentences so your message stays simple, honest and easy for customers to follow.</p></div>
      <div class="field"><div class="field-label">Weaknesses :</div><p class="field-hint">Describe this in a few clear sentences so your message stays simple, honest and easy for customers to follow.</p></div>
      <div class="field"><div class="field-label">Opportunities :</div><p class="field-hint">Describe this in a few clear sentences so your message stays simple, honest and easy for customers to follow.</p></div>
      <div class="field"><div class="field-label">Threats :</div><p class="field-hint">Describe this in a few clear sentences so your message stays simple, honest and easy for customers to follow.</p></div>
    </div>
  </section>

  <h2 class="section-title why">WHY YOU EXIST</h2>
  <div class="grid why">
    <div class="field"><div class="field-label">Who are your ideal customers?</div><p class="field-hint">Describe this in a few clear sentences so your message stays simple, honest and easy for customers to follow.</p><svg class="help" viewBox="0 0 16 16"><circle cx="8" cy="8" r="7" fill="#b5b5b5"/><text x="8" y="12" text-anchor="middle" font-size="10" fill="#fff" font-family="Montserrat,sans-serif">?</text></svg></div>
    <div class="field"><div class="field-label">What problem are you trying to solve for them?</div><p class="field-hint">Describe this in a few clear sentences so your message stays simple, honest and easy for customers to follow.</p><svg class="help" viewBox="0 0 16 16"><circle cx="8" cy="8" r="7" fill="#b5b5b5"/><text x="8" y="12" text-anchor="middle" font-size="10" fill="#fff" font-family="Montserrat,sans-serif">?</text></svg></div>
    <div class="field"><div class="field-label">What pain points will this remove for them?</div><p class="field-hint">Describe this in a few clear sentences so your message stays simple, honest and easy for customers to follow.</p><svg class="help" viewBox="0 0 16 16"><circle cx="8" cy="8" r="7" fill="#b5b5b5"/><text x="8" y="12" text-anchor="middle" font-size="10" fill="#fff" font-family="Montserrat,sans-serif">?</text></svg></div>
    <div class="field"><div class="field-label">How do you solve it?</div><p class="field-hint">Describe this in a few clear sentences so your message stays simple, honest and easy for customers to follow.</p><svg class="help" viewBox="0 0 16 16"><circle cx="8" cy="8" r="7" fill="#b5b5b5"/><text x="8" y="12" text-anchor="middle" font-size="10" fill="#fff" font-family="Montserrat,sans-serif">?</text></svg></div>
    <div class="field"><div class="field-label">How else could this problem be solved?</div><p class="field-hint">Describe this in a few clear sentences so your message stays simple, honest and easy for customers to follow.</p><svg class="help" viewBox="0 0 16 16"><circle cx="8" cy="8" r="7" fill="#b5b5b5"/><text x="8" y="12" text-anchor="middle" font-size="10" fill="#fff" font-family="Montserrat,sans-serif">?</text></svg></div>
    <div class="field"><div class="field-label">Who offers these other solutions?</div><p class="field-hint">Describe this in a few clear sentences so your message stays simple, honest and easy for customers to follow.</p><svg class="help" viewBox="0 0 16 16"><circle cx="8" cy="8" r="7" fill="#b5b5b5"/><text x="8" y="12" text-anchor="middle" font-size="10" fill="#fff" font-family="Montserrat,sans-serif">?</text></svg></div>
    <div class="field"><div class="field-label">Why is your solution better?</div><p class="field-hint">Describe this in a few clear sentences so your message stays simple, honest and easy for customers to follow.</p><svg class="help" viewBox="0 0 16 16"><circle cx="8" cy="8" r="7" fill="#b5b5b5"/><text x="8" y="12" text-anchor="middle" font-size="10" fill="#fff" font-family="Montserrat,sans-serif">?</text></svg></div>
    <div class="field"><div class="field-label">How much does your solution cost?</div><p class="field-hint">Describe this in a few clear sentences so your message stays simple, honest and easy for customers to follow.</p><svg class="help" viewBox="0 0 16 16"><circle cx="8" cy="8" r="7" fill="#b5b5b5"/><text x="8" y="12" text-anchor="middle" font-size="10" fill="#fff" font-family="Montserrat,sans-serif">?</text></svg></div>
    <div class="field"><div class="field-label">What value are you providing to justify this cost?</div><p class="field-hint">Describe this in a few clear sentences so your message stays simple, honest and easy for customers to follow.</p><svg class="help" viewBox="0 0 16 16"><circle cx="8" cy="8" r="7" fill="#b5b5b5"/><text x="8" y="12" text-anchor="middle" font-size="10" fill="#fff" font-family="Montserrat,sans-serif">?</text></svg></div>
    <div class="field"><div class="field-label">How will this make their life/job easier/better?</div><p class="field-hint">Describe this in a few clear sentences so your message stays simple, honest and easy for customers to follow.</p><svg class="help" viewBox="0 0 16 16"><circle cx="8" cy="8" r="7" fill="#b5b5b5"/><text x="8" y="12" text-anchor="middle" font-size="10" fill="#fff" font-family="Montserrat,sans-serif">?</text></svg></div>
  </div>

  <button class="save" type="button">Save Changes</button>
</main>

<footer class="footer">© Copy Right 2017 Tendril All rights reserved</footer>

</body>
</html>
```